Cosmetic Dentist Practice needs stationery package/logo

I need a letterhead, envelope and business card for a cosmetic and Dental Inplant practice in an upscale part of Houston. The business card will be a size 3.5 x 2 and the letterhead will be 8.5" x 11" with a standard #10 envelope.
I have uploaded a file with an idea that the dentist had for his cards. Please note that this is not the size that the card should be. It does provide the information required.
Thank you all for your submissions. They were each unique and special in their own way. My client has made a selection that he feels best meets his needs. I appreciate each of you taking the time to offer designs. Good luck to each of you...I hope to see you back in Sketchforum on future projects.

```html
<!DOCTYPE html>
<html lang="en">
<head>
<meta charset="utf-8">
<title>Letterhead – Midtown Smile &amp; Implant Studio</title>
<link href="https://fonts.googleapis.com/css2?family=Open+Sans:wght@400;600&display=swap" rel="stylesheet">
<style>
  :root {
    --backdrop: #9a9a9a;
    --paper: #ffffff;
    --brand: #8b3a46;
    --ink: #7a3440;
  }
  * { margin: 0; padding: 0; box-sizing: border-box; }
  html, body { width: 1200px; height: 1200px; overflow: hidden; }
  body {
    background: var(--backdrop);
    font-family: "Open Sans", sans-serif;
    color: var(--ink);
    position: relative;
  }
  .letterhead {
    position: absolute;
    left: 175px; top: 50px;
    width: 850px; height: 1100px;
    background: var(--paper);
    box-shadow: 0 6px 24px rgba(0,0,0,.25);
  }
  .brand {
    position: absolute;
    left: 70px; top: 62px;
    display: flex; align-items: center; gap: 14px;
  }
  .brand-dot {
    width: 34px; height: 34px;
    border-radius: 50%;
    background: var(--brand);
  }
  .brand-name {
    font-size: 26px; font-weight: 400;
    line-height: 1.15; letter-spacing: 1.5px;
    text-transform: uppercase;
    color: var(--brand);
  }
  .header-rule {
    position: absolute;
    left: 40px; top: 200px;
    width: 540px; height: 3px;
    background: var(--brand);
  }
  .practice-details {
    position: absolute;
    left: 590px; top: 138px;
    width: 210px;
    font-style: normal;
    white-space: nowrap;
    font-size: 14px; line-height: 1.35;
  }
  .practice-details .doctor { font-weight: 600; }
  .dotted-rule { border-top: 3px dotted var(--brand); }
  .header-dots {
    position: absolute;
    left: 590px; width: 200px; top: 200px;
  }
  .footer {
    position: absolute;
    left: 70px; bottom: 90px;
    font-size: 13px; line-height: 1.6;
  }
  .footer .footer-dots { width: 120px; margin: 0 0 8px 90px; }
  .footer .address { padding-left: 90px; }
  .contact-row { display: flex; gap: 18px; align-items: center; }
  .contact-item { display: inline-flex; align-items: center; gap: 5px; }
  .contact-item svg { width: 13px; height: 13px; fill: var(--brand); }
</style>
</head>
<body>
  <main class="letterhead">
    <header>
      <div class="brand">
        <span class="brand-dot"></span>
        <span class="brand-name">Midtown Smile &amp;<br>Implant Studio</span>
      </div>
      <div class="header-rule"></div>
      <address class="practice-details">
        <div class="doctor">Adrian Montoya, D.D.S., PLLC.</div>
        <div>84 Cedar Ridge Lane Suite 210</div>
        <div>W. Houston, TX. 77000</div>
      </address>
      <div class="dotted-rule header-dots"></div>
    </header>

    <footer class="footer">
      <div class="dotted-rule footer-dots"></div>
      <div class="address">84 Cedar Ridge Lane Suite 210 W. Houston, TX. 77000</div>
      <div class="contact-row">
        <span class="contact-item">
          <svg viewBox="0 0 24 24"><path d="M6.6 10.8a15 15 0 0 0 6.6 6.6l2.2-2.2c.3-.3.7-.4 1-.2 1.1.4 2.3.6 3.6.6.6 0 1 .4 1 1V20c0 .6-.4 1-1 1A17 17 0 0 1 3 4c0-.6.4-1 1-1h3.5c.6 0 1 .4 1 1 0 1.3.2 2.5.6 3.6.1.3 0 .7-.2 1z"/></svg>
          555-010-4821
        </span>
        <span class="contact-item">
          <svg viewBox="0 0 24 24"><path d="M5 8h14a2 2 0 0 1 2 2v7H3v-7a2 2 0 0 1 2-2zm2-5h10v4H7zm0 11h10v7H7z"/></svg>
          555-010-4836
        </span>
        <span class="contact-item">
          <svg viewBox="0 0 24 24"><path d="M3 5h18v14H3zm2 2v.5l7 5 7-5V7zm0 3v7h14v-7l-7 5z"/></svg>
          DrMontoya@msistudio.com
        </span>
      </div>
    </footer>
  </main>
</body>
</html>
```